Craft Beer Needs a Label/ Logo Design

Name: Lanternfall
(Lanternfall Ale, Lanternfall Pilsner, Lanternfall Stout)

We are looking for a logo-ed label that will resonate domestically and internationally for this new Craft Beer Brand.

Target Market(s)

Millenials

Logo Text

Lanternfall Pilsner

Logo styles of interest
Emblem Logo
Character Logo
Colors

Designer to choose colors to be used in the design.

Requirements
Must have
• A labled logo design -- "Lanternfall" is the name, but would like to see samples with "Ale", "Pilsner", or "Stout" after!

```html
<!DOCTYPE html>
<html lang="en">
<head>
<meta charset="utf-8">
<title>Lanternfall Ale Label</title>
<link rel="stylesheet" href="https://fonts.googleapis.com/css2?family=Bebas+Neue&family=Oswald:wght@500&family=Pinyon+Script&display=swap">
<style>
  :root {
    --page: #ffffff;
    --shield-deep: #0b2440;
    --shield-mid: #1a3d63;
    --dial-light: #d6f0f2;
    --dial-mid: #9cc2d0;
    --dial-edge: #34567a;
    --ribbon-face: #80a6b9;
    --ribbon-tail: #6c93a7;
    --ribbon-fold: #3e6276;
    --ink-white: #ffffff;
    --ink-black: #0a0a0a;
  }
  html, body {
    margin: 0;
    padding: 0;
    width: 1200px;
    height: 1200px;
    overflow: hidden;
    background: var(--page);
  }
  .label-canvas {
    width: 1200px;
    height: 1200px;
    display: block;
  }
  .shield {
    filter: drop-shadow(22px 26px 18px rgba(0, 0, 0, 0.55));
  }
  .ribbon {
    filter: drop-shadow(6px 14px 10px rgba(0, 0, 0, 0.45));
  }
  .brand-name {
    font-family: "Bebas Neue", "Oswald", sans-serif;
    font-size: 172px;
    letter-spacing: 1px;
  }
  .brand-name .light { fill: var(--ink-white); }
  .brand-name .dark { fill: var(--ink-black); }
  .beer-style {
    font-family: "Pinyon Script", cursive;
    font-size: 150px;
    fill: var(--ink-white);
    filter: drop-shadow(3px 3px 3px rgba(0, 0, 0, 0.7));
  }
  .brewery-line {
    font-family: "Oswald", sans-serif;
    font-weight: 500;
    font-size: 54px;
    fill: var(--ink-white);
    letter-spacing: 1px;
  }
</style>
</head>
<body>
<svg class="label-canvas" viewBox="0 0 1200 1200" xmlns="http://www.w3.org/2000/svg">
  <defs>
    <radialGradient id="shield-glow" cx="600" cy="470" r="560" gradientUnits="userSpaceOnUse">
      <stop offset="0" stop-color="#6f93b3"/>
      <stop offset="0.55" stop-color="var(--shield-mid)"/>
      <stop offset="1" stop-color="var(--shield-deep)"/>
    </radialGradient>
    <radialGradient id="dial-fill" cx="600" cy="390" r="360" gradientUnits="userSpaceOnUse">
      <stop offset="0" stop-color="var(--dial-light)"/>
      <stop offset="0.55" stop-color="var(--dial-mid)"/>
      <stop offset="1" stop-color="var(--dial-edge)"/>
    </radialGradient>
  </defs>

  <path class="shield" fill="url(#shield-glow)"
        d="M233 258 Q233 213 278 213 L922 213 Q967 213 967 258 L967 745
           C967 895 770 1010 600 1113 C430 1010 233 895 233 745 Z"/>

  <g class="clock-dial" role="img" aria-label="Clock face with roman numerals and hands pointing to twelve">
    <circle cx="600" cy="395" r="362" fill="#1c3956"/>
    <circle cx="600" cy="395" r="340" fill="url(#dial-fill)"/>
  </g>

  <g class="ribbon">
    <polygon fill="var(--ribbon-tail)" points="60,520 233,520 233,665 60,665 125,592"/>
    <polygon fill="var(--ribbon-fold)" points="175,617 233,617 233,665"/>
    <polygon fill="var(--ribbon-tail)" points="1140,520 967,520 967,665 1140,665 1075,592"/>
    <polygon fill="var(--ribbon-fold)" points="1025,617 967,617 967,665"/>
    <rect fill="var(--ribbon-face)" x="175" y="483" width="850" height="134"/>
  </g>

  <text class="brand-name" x="600" y="612" text-anchor="middle"><tspan class="light">LANTERN</tspan><tspan class="dark">FALL</tspan></text>

  <text class="beer-style" x="590" y="720" text-anchor="middle">Ale</text>

  <text class="brewery-line" x="600" y="888" text-anchor="middle">LANTERNFALL CRAFT BREWS</text>
  <text class="brewery-line" x="600" y="973" text-anchor="middle">BREWTOWN, ST</text>
</svg>
</body>
</html>
```